Road Keeper Community Awareness Poster

We are looking for a tabloid size (11"x17") Poster to be placed all over various towns and communities promoting our business. We need something that grabs the attention of our target demographic (parents of teen drivers) and gets them to want to learn more about our programs and ultimately sign up for one of our events.

see our website for more information at www.roadkeeperhub.example

Target Market(s)

We want parents of teens ages 15 - 19 to be aware how dangerous driving is for new drivers and compel them to sign their teen up for our program.

Industry/Entity Type

Community

Requirements
Must have
• Must have our logo and identity, url and be 11"x17"

```html
<!DOCTYPE html>
<html lang="en">
<head>
<meta charset="utf-8">
<title>Road Keeper – Teen Car Control Poster</title>
<link href="https://fonts.googleapis.com/css2?family=Anton&family=Oswald:wght@500&family=Roboto+Condensed:wght@400;700&display=swap" rel="stylesheet">
<style>
  :root {
    --backdrop: #e9e6e1;
    --poster-dark: #141414;
    --poster-mid: #3a3a3a;
    --brand-green: #2fae2b;
    --white: #ffffff;
    --photo-dark: #1c1d1f;
    --photo-mid: #6b6d70;
    --photo-light: #c9c9c9;
  }
  * { margin: 0; padding: 0; box-sizing: border-box; }
  html, body {
    width: 904px; height: 1200px; overflow: hidden;
    background: var(--backdrop);
  }
  .poster {
    position: absolute; left: 82px; top: 25px;
    width: 740px; height: 1150px; overflow: hidden;
    background:
      radial-gradient(ellipse at 50% 30%, var(--poster-mid) 0%, var(--poster-dark) 75%);
    color: var(--white);
    text-align: center;
  }
  .brand {
    position: absolute; left: 0; right: 0; top: 60px;
    display: flex; flex-direction: column; align-items: center; gap: 18px;
  }
  .brand-dot {
    width: 92px; height: 92px; border-radius: 50%;
    background: var(--brand-green);
  }
  .brand-name {
    font-family: "Roboto Condensed", sans-serif; font-weight: 700;
    font-size: 30px; letter-spacing: 1px; color: var(--white);
    line-height: 1;
  }
  .headline {
    position: absolute; left: 0; right: 0; top: 205px;
    font-family: "Anton", sans-serif; font-size: 92px; line-height: 1;
    color: var(--white); letter-spacing: 1px;
    -webkit-text-stroke: 3px var(--brand-green);
    paint-order: stroke fill;
  }
  .subhead {
    position: absolute; left: 0; right: 0; top: 318px;
    font-family: "Anton", sans-serif; font-size: 38px; line-height: 1;
    color: var(--brand-green); letter-spacing: 19px; padding-left: 19px;
    -webkit-text-stroke: 1px var(--white);
    paint-order: stroke fill;
  }
  .photo {
    position: absolute; left: 0; right: 0; top: 395px; height: 470px;
    background:
      radial-gradient(ellipse at 72% 45%, var(--photo-light) 0%, transparent 40%),
      linear-gradient(170deg, var(--photo-mid) 0%, var(--photo-dark) 55%, var(--poster-dark) 100%);
  }
  .tagline {
    position: absolute; left: 0; right: 0; top: 902px;
    font-family: "Roboto Condensed", sans-serif; font-weight: 400;
    font-size: 26px; line-height: 1; text-transform: uppercase;
  }
  .rule {
    position: absolute; left: 48px; right: 48px; height: 5px;
    background: var(--white);
  }
  .rule-top { top: 942px; }
  .rule-bottom { top: 1060px; }
  .course {
    position: absolute; left: 0; right: 0; top: 950px;
    font-family: "Oswald", sans-serif; font-weight: 500;
    font-size: 74px; line-height: 1.2; color: var(--brand-green);
    transform: scaleX(0.92);
  }
  .web-address {
    position: absolute; left: 0; right: 0; top: 1080px;
    font-family: "Roboto Condensed", sans-serif; font-weight: 400;
    font-size: 38px; line-height: 1; letter-spacing: 5px; padding-left: 5px;
  }
</style>
</head>
<body>
  <main class="poster">
    <header class="brand">
      <span class="brand-dot"></span>
      <span class="brand-name">ROAD KEEPER</span>
    </header>
    <h1 class="headline">TEEN CAR CONTROL</h1>
    <h2 class="subhead">DRIVING KNOWLEDGE</h2>
    <div class="photo" role="img" aria-label="Smiling young woman behind the steering wheel of a silver car, looking out of the open driver's window"></div>
    <p class="tagline">Improve teen car control and overall safety</p>
    <div class="rule rule-top"></div>
    <p class="course">Defensive driving course</p>
    <div class="rule rule-bottom"></div>
    <p class="web-address">www.roadkeeperhub.example</p>
  </main>
</body>
</html>
```